Meridian Vault Data Systems Needs a Website Desing

We need a website design for a new company based in Kuwait called Meridian Vault Data Systems (MVDS). We provide Software as a Service (SaaS) solutions for small and medium business companies. We will develop the required E-systems like HR,Payroll,Accounting Systems for those customers who wants to focus on their business instead of wasting time to automate it. MVDS need a web site that represent this activity and showing our cloud products and allow out customers to easily identify their needs. as a normal web site basic things need to be included like :
about MVDS
Solutions
PressRoom
Contact us
please i need something similar to qorlix.com or tuv.com or www.hxp7zul.com with blue and black theme .. please check the Company's logo
hi all ,,,
the project is only design without any codes
Reason: The project is focus on design only ,, i will be really appreciated to have more designs

```html
<!DOCTYPE html>
<html lang="en">
<head>
<meta charset="utf-8">
<title>MVDS – Software as a Service Solutions</title>
<link href="https://fonts.googleapis.com/css2?family=Ubuntu:wght@400;500;700&family=Noto+Serif&display=swap" rel="stylesheet">
<style>
:root{
  --blue:#1e8fd6;
  --blue-light:#45b2ee;
  --link:#2a8fd2;
  --footer-link:#4ab3ee;
  --ink:#333;
  --text:#555;
  --muted:#777;
  --band-dark:#333;
  --panel:#f2f2f2;
  --footer:#3a3a3a;
  --hero:#2cb6ee;
}
*{margin:0;padding:0;box-sizing:border-box}
html,body{width:1029px;height:1200px;overflow:hidden;background:#fff}
body{font-family:"Ubuntu",Arial,sans-serif;color:var(--text)}
a{text-decoration:none;color:inherit}
.page{position:relative;width:1200px;height:1400px;transform:scale(.8575);transform-origin:0 0;
  background:linear-gradient(#f0f0f0 0,#f4f4f4 124px,#3c3c3c 124px,#2e2e2e 549px,#f7f7f7 549px,#f7f7f7 613px,#fff 613px,#fff 792px,var(--panel) 792px,var(--panel) 1075px,#fff 1075px)}
.abs{position:absolute}

.brand{left:130px;top:22px;display:flex;align-items:center;gap:10px;color:#222;font-weight:700}
.brand-mark{width:66px;height:66px;border-radius:50%;background:var(--blue)}
.brand-name{font-size:50px;line-height:48px;letter-spacing:-1px}
.brand-full{font-size:10px;line-height:12px;display:block;letter-spacing:0}

.utility{right:130px;top:12px;font-size:11px;color:#444}
.utility .loc{color:var(--link)}
.utility .sep{color:var(--link);margin:0 8px}
.tagline{right:131px;top:41px;font-size:20px;color:var(--blue);font-weight:500;text-align:right}
.subline{right:131px;top:68px;font-size:13px;color:#444}

.nav{left:130px;top:101px;width:940px;height:52px;border-radius:4px;background:linear-gradient(#4cb4ef,#1f8ad1)}
.nav a{position:absolute;top:19px;font-size:13px;color:#fff;font-weight:500}
.search{position:absolute;left:720px;top:13px;width:206px;height:27px;background:#fff;border-radius:4px}
.search svg{position:absolute;right:4px;top:3px}

.hero{left:130px;top:166px;width:940px;height:396px;border:2px solid #fff;box-shadow:0 8px 14px -8px rgba(0,0,0,.35);overflow:hidden}
.hero-art{position:absolute;inset:0;background:radial-gradient(circle at 230px 230px,#164a7a 0,#0d2c4c 150px,transparent 230px),linear-gradient(90deg,#0a1f36 0,#1d87c8 38%,var(--hero) 55%,#4cc3f2 100%)}
.hero-text{position:absolute;right:38px;top:86px;text-align:right;color:#fff;font-size:38px;line-height:46px;font-weight:500;text-shadow:0 2px 4px rgba(0,0,0,.35)}
.hero-text .accent{color:#2a3b4c;text-shadow:0 1px 2px rgba(255,255,255,.3)}
.dots{position:absolute;left:403px;bottom:0;width:134px;height:30px;background:#1f8ad1;border-radius:8px 8px 0 0;display:flex;gap:7px;justify-content:center;align-items:center}
.dots i{width:14px;height:14px;border-radius:50%;background:#e8e8e8}
.dots i.on{background:#222}

.sidebar{left:1169px;top:407px;width:31px;height:138px;background:#fff;border:1px solid #ccc;border-radius:3px 0 0 3px;padding:10px 6px;display:flex;flex-direction:column;gap:8px}
.sidebar i{width:16px;height:16px;background:#8a8a8a;border-radius:2px}

.card{top:601px;width:300px;height:154px;border:1px solid #d6d6d6;background:linear-gradient(#fff,#e6e6e6);box-shadow:0 6px 8px -6px rgba(0,0,0,.35)}
.card h3{position:absolute;z-index:2;left:27px;top:18px;font-size:32px;line-height:30px;font-weight:500;color:#555;white-space:nowrap}
.card h3 span{display:block;font-size:26px;color:var(--blue);font-weight:400}
.card .more{position:absolute;z-index:2;left:27px;top:119px;font-size:12px;color:#555}
.card .art{position:absolute;z-index:1;right:12px;top:58px;width:118px;height:88px;border-radius:8px}

.col{top:826px;width:300px}
.col h2{font-size:20px;font-weight:500;color:var(--ink);margin-bottom:14px}
.col p{font-size:12px;line-height:23px;color:var(--text)}
.col .cta{position:absolute;top:202px;font-size:13px;color:var(--link)}
.date{position:absolute;left:-2px;top:40px;width:84px;height:74px;border:2px solid #ddd;background:#fff;text-align:center;font-family:"Noto Serif",Georgia,serif;color:#555;box-shadow:0 8px 8px -6px rgba(0,0,0,.3)}
.date .m{font-size:14px;color:var(--blue);line-height:18px;margin-top:2px}
.date .d{font-size:34px;line-height:34px}
.date .y{background:#4aa6de;color:#fff;font-size:13px;line-height:16px;margin-top:2px}
.tweet-meta{font-size:12px;color:var(--link);margin-top:12px}
.tweet-meta b{font-weight:400;color:#999;margin:0 8px}

.footer{left:130px;top:1091px;width:940px;height:237px;background:var(--footer);border-radius:4px}
.fcol{position:absolute;top:24px}
.fcol h4{font-size:14px;color:#fff;font-weight:500;margin-bottom:6px}
.fcol a{display:block;font-size:12.5px;line-height:25px;color:var(--footer-link)}

.copy{left:130px;top:1357px;font-size:12px;color:#888}
.copy a{color:var(--link)}
.social{right:130px;top:1358px;display:flex;align-items:center;gap:10px;font-size:9px;color:#999;letter-spacing:1px}
.social i{width:14px;height:14px;border-radius:50%;background:#aaa;display:inline-block}
.social .bar{color:#ccc}
</style>
</head>
<body>
<div class="page">

  <div class="abs brand">
    <span class="brand-mark"></span>
    <span><span class="brand-name">MVDS</span><span class="brand-full">Meridian Vault Data Systems</span></span>
  </div>

  <div class="abs utility">Location : <span class="loc">United State ▾</span><span class="sep">|</span>My Account</div>
  <div class="abs tagline">We provide Software as a Service (SaaS) Solutions</div>
  <div class="abs subline">for small and medium business companies</div>

  <nav class="abs nav">
    <a href="#" style="left:23px">HOME</a>
    <a href="#" style="left:132px">ABOUT MVDS</a>
    <a href="#" style="left:284px">SOLUTIONS</a>
    <a href="#" style="left:424px">PRESS ROOM</a>
    <a href="#" style="left:574px">CONTACT US</a>
    <div class="search">
      <svg width="22" height="22" viewBox="0 0 22 22"><circle cx="9" cy="9" r="6" fill="none" stroke="#333" stroke-width="2.5"/><line x1="13.5" y1="13.5" x2="20" y2="19" stroke="#333" stroke-width="3.5" stroke-linecap="round"/></svg>
    </div>
  </nav>

  <section class="abs hero">
    <div class="hero-art" role="img" aria-label="Glass globe with cloud icon over a blue cloud background"></div>
    <div class="hero-text">We provide Software as a<br>Service <span class="accent">(SaaS)</span> solutions for<br>small and medium business<br>companies</div>
    <div class="dots"><i class="on"></i><i></i><i></i><i></i><i></i></div>
  </section>

  <div class="abs sidebar"><i></i><i></i><i></i><i></i><i></i></div>

  <div class="abs card" style="left:130px">
    <h3>HR<span>SOLUTION</span></h3>
    <a class="more" href="#">LEARN MORE&gt;&gt;</a>
    <div class="art" role="img" aria-label="Coloured puzzle cube" style="background:linear-gradient(135deg,#e8c22a,#d33 45%,#2339a0 60%,#1a2a70)"></div>
  </div>
  <div class="abs card" style="left:450px">
    <h3>PAYROLL<span>SOLUTION</span></h3>
    <a class="more" href="#">LEARN MORE&gt;&gt;</a>
    <div class="art" role="img" aria-label="Paper payroll sack spilling peanuts" style="background:linear-gradient(135deg,#e6c9a8,#c79a6b 55%,#e9d2a6)"></div>
  </div>
  <div class="abs card" style="left:770px">
    <h3>ACCOUNTING<span>SOLUTION</span></h3>
    <a class="more" href="#">LEARN MORE&gt;&gt;</a>
    <div class="art" role="img" aria-label="Red and grey currency symbols" style="background:linear-gradient(135deg,#e9e9e9,#e05a5a 45%,#c9c9c9 75%)"></div>
  </div>

  <section class="abs col" style="left:131px">
    <h2>ABOUT MVDS</h2>
    <p>Aliquam molestie, mi et imperdiet euismod, dui purus auctor tellus, et interdum lacus lectus et ante. Sed accumsan sollicitudin sapien, sit amet adipiscing turpis gravida ac. In congue, neque ac lobortis volutpat, libero mauris varius mi, vitae suscipit ipsum ligula vitae risus.</p>
    <a class="cta" href="#">LEARN MORE</a>
  </section>

  <section class="abs col" style="left:451px">
    <h2>PRESS ROOM</h2>
    <div class="date"><div class="m">MAY</div><div class="d">02</div><div class="y">2013</div></div>
    <p style="margin-left:99px;width:200px">Aliquam molestie, mi et imperdiet euismod, dui purus auctor tellus, et interdum lacus lectus et ante. Sed accumsan sollicitudin sapien, sit amet adipiscing turpis gravida ac.</p>
    <a class="cta" href="#">READ ALL NEWS</a>
  </section>

  <section class="abs col" style="left:780px;width:295px">
    <h2>CHIRPER</h2>
    <p>Dui purus auctor tellus, et interdum lacus lectus et ante<a href="#" style="color:var(--blue);font-weight:500">http://ch.rp/c72KY6jVoN</a> sapien, sit amet adipiscing turpis gravida ac.</p>
    <div class="tweet-meta">8 hours ago<b>|</b>Reply<b>|</b>Rechirp<b>|</b>Favorite</div>
    <a class="cta" href="#" style="left:-1px">READ ALL CHIRPS</a>
  </section>

  <footer class="abs footer">
    <div class="fcol" style="left:45px"><h4>SITE NAVIGATION</h4><a href="#">Home</a><a href="#">About MVDS</a><a href="#">Solutions</a><a href="#">Press Room</a><a href="#">Contact Us</a></div>
    <div class="fcol" style="left:216px"><h4>SOCIAL @ MVDS</h4><a href="#">Recent Blog Posts</a><a href="#">All MVDS Blogs</a><a href="#">MVDS Community Network</a><a href="#">Friendwall</a><a href="#">Chirper</a><a href="#">ClipStream</a><a href="#">WorkLink</a></div>
    <div class="fcol" style="left:418px"><h4>LEARNING</h4><a href="#">Training and Certification</a><a href="#">Corvane Security Training</a><a href="#">MVDS Academic Alliance</a><a href="#">MVDS Proven Professional</a><a href="#">Partner Readiness</a><a href="#">Events</a><a href="#">Resource Library</a></div>
    <div class="fcol" style="left:616px"><h4>PARTNERS</h4><a href="#">View MVDS Partners</a><a href="#">Partner Resources</a><a href="#">Partner Community</a><a href="#">Velocity Program</a><a href="#">Corvane Partners</a><a href="#">Partner Solution Gallery</a><a href="#">Partnerlink Login</a></div>
    <div class="fcol" style="left:800px"><h4>POPULAR</h4><a href="#">About Tuvex</a><a href="#">Investor Relations</a><a href="#">Careers @ MVDS</a><a href="#">Newsroom</a><a href="#">Sustainability</a><a href="#">MVDS MOBILE</a><a href="#">Product Security</a></div>
  </footer>

  <div class="abs copy">© 2013 <a href="#">MVDS</a>. All rights reserved.</div>
  <div class="abs social">
    <span>SHARE</span><i></i><span class="bar">|</span><span>FOLLOW</span><i></i><i></i><i></i><i></i><i></i><span class="bar">|</span><span>RSS</span><i></i>
  </div>

</div>
</body>
</html>
```